Wooden Floor Website

I'd like a Modern and crisp site with emphasis on the site being easy to navigate through - services that we offer, gallery of previous work, history, who we are, contact, etc
https://tmqrvx8219067-my.dokshelfbox.net/:b:/g/personal/marcus_bellhaven_co_uk/QWT7K2_pmRsNaHXdovtYBeLWCKjuP9e3F6kRMZbqUwnPzs

Coding

Coded - Design and coding required

Number of Pages Required

5+ page

Requirements
Must have
• Word Press Site

```html
<!DOCTYPE html>
<html lang="en">
<head>
<meta charset="utf-8">
<title>Bellhaven – Bespoke Wood Flooring</title>
<link rel="stylesheet" href="https://fonts.googleapis.com/css2?family=IBM+Plex+Sans:wght@400;500;600&family=Lato:wght@400;700&display=swap">
<style>
:root{
  --paper:#f7f5ef;
  --ink:#1d1d1d;
  --text:#4a4a4a;
  --black:#141414;
  --nav-active:#3a3a3a;
  --white:#ffffff;
  --wood-dark:#5a4632;
  --wood-mid:#7d6149;
  --wood-warm:#8e6c45;
  --wood-light:#b4936d;
  --line:#cfcac0;
}
*{box-sizing:border-box;margin:0;padding:0}
html,body{width:1200px;height:3930px;overflow:hidden}
body{background:var(--paper);font-family:"Lato",sans-serif;color:var(--text);position:relative}
h1,h2,h3,h4{font-family:"IBM Plex Sans",sans-serif;font-weight:400;color:var(--ink)}
.btn{display:inline-block;background:var(--black);color:var(--white);font-size:13px;padding:0 28px;line-height:42px;text-decoration:none;font-family:"Lato",sans-serif}
section,header,nav,footer{position:absolute;left:0;width:1200px}

/* top bar */
.topbar{top:0;height:110px;background:var(--paper)}
.social{position:absolute;display:flex;gap:8px}
.social span{width:18px;height:18px;border-radius:50%;background:var(--ink);display:block}
.topbar .social{left:81px;top:46px}
.brand{position:absolute;left:0;width:1200px;top:34px;text-align:center;font-family:"IBM Plex Sans",sans-serif;font-weight:600;font-size:15px;letter-spacing:2px;color:var(--ink)}
.brand small{display:block;font-weight:400;font-size:10px;letter-spacing:1px;margin-top:6px;color:var(--ink)}
.callus{position:absolute;right:82px;top:38px;display:flex;gap:10px;align-items:center;font-size:12px;color:var(--ink);line-height:1.3}

/* nav */
.mainnav{top:110px;height:52px;background:var(--black)}
.mainnav a{position:absolute;top:0;color:var(--white);text-decoration:none;font-size:14px;width:143px;text-align:center;line-height:52px;height:52px;white-space:nowrap}
.mainnav a.active{background:var(--nav-active);width:110px;left:80px;font-weight:700}
.mainnav .search{position:absolute;right:82px;top:14px}

/* hero */
.hero{top:162px;height:528px}
.hero-photo{position:absolute;inset:0;background:linear-gradient(90deg,#d9dadb 0,#cfcfcd 17%,#7f6e5e 22%,#8b7663 50%,#735f4d 80%,#8a7561 100%)}
.hero-copy{position:absolute;left:0;width:1200px;top:200px;text-align:center}
.hero-copy h1{color:var(--white);font-size:40px;line-height:48px}
.btn-outline{display:inline-block;margin-top:30px;border:1px solid var(--white);color:var(--white);font-size:13px;width:146px;line-height:40px;text-decoration:none}
.dots{position:absolute;top:494px;left:552px;display:flex;gap:6px}
.dots i{width:20px;height:3px;background:rgba(255,255,255,.6);display:block}
.dots i:first-child{background:var(--white)}

/* about */
.about{top:690px;height:360px;text-align:center}
.about h2{font-size:32px;margin-top:62px}
.about p{width:700px;margin:22px auto 0;font-size:13px;line-height:18px;color:var(--text)}
.about p + p{margin-top:16px}
.about .btn{margin-top:26px;width:150px;padding:0}

/* services */
.services{top:1050px;height:560px;text-align:center}
.services h2{font-size:32px;margin-top:0}
.services .lead{width:360px;margin:4px auto 0;font-size:13px;line-height:16px}
.service-list{display:flex;position:absolute;top:123px;left:66px}
.service{width:276px;text-align:center}
.service .photo{width:245px;height:245px;border-radius:50%;margin:0 auto}
.service h3{font-size:18px;margin-top:30px}
.service h3::after{content:"";display:block;width:64px;height:3px;background:var(--ink);margin:10px auto 0}
.service p{width:220px;margin:16px auto 0;font-size:13px;line-height:16px}
.service a{display:inline-block;margin-top:12px;font-size:13px;color:var(--text)}

/* process */
.process{top:1650px;height:357px}
.process-bg{position:absolute;inset:0;background:linear-gradient(90deg,#e6ddd4,#ded4ca 50%,#e4dbd2)}
.process h2{position:absolute;top:20px;left:0;width:1200px;text-align:center;font-size:32px;letter-spacing:.5px;font-weight:400}
.step{position:absolute;top:92px;width:190px;text-align:center}
.step .num{width:160px;height:160px;border-radius:50%;margin:0 auto;color:var(--white);font-family:"IBM Plex Sans",sans-serif;font-size:50px;line-height:160px}
.step p{margin-top:12px;font-size:18px;line-height:22px;color:var(--ink);font-family:"IBM Plex Sans",sans-serif}
.arrow{position:absolute;top:142px}

/* gallery */
.gallery{top:2007px;height:760px}
.gallery h2{text-align:center;font-size:32px;margin-top:52px}
.gallery-grid{position:absolute;top:118px;left:81px;display:grid;grid-template-columns:328px 330px 327px;column-gap:26px;row-gap:28px}
.gallery-grid div{height:252px}
.gallery .btn{position:absolute;top:689px;left:529px;width:144px;padding:0;text-align:center}

/* history */
.history{top:2767px;height:429px}
.history-copy{position:absolute;left:162px;top:90px;width:400px}
.history h2{font-size:32px}
.history p{font-size:13px;line-height:17px;margin-top:18px}
.history p + p{margin-top:14px}
.history .btn{margin-top:26px;width:144px;padding:0;text-align:center}
.history-photos{position:absolute;left:676px;top:71px;width:351px;height:293px}

/* contact */
.contact{top:3196px;height:367px}
.contact-bg{position:absolute;inset:0;background:linear-gradient(110deg,#6e5a48 0,#9a8470 18%,#a8937f 45%,#95806b 75%,#7c6855 100%)}
.contact h2{position:absolute;top:38px;left:0;width:1200px;text-align:center;color:var(--white);font-size:32px}
.field{position:absolute;border:1px solid rgba(255,255,255,.9);color:var(--white);font-size:13px;padding:6px 8px;height:38px}
.contact .btn{position:absolute;left:527px;top:286px;width:144px;padding:0;text-align:center}

/* footer */
.site-footer{top:3563px;height:293px;background:var(--black);color:var(--white)}
.site-footer h4{color:var(--white);font-size:14px;font-family:"IBM Plex Sans",sans-serif;font-weight:500}
.foot-brand{position:absolute;left:80px;top:80px;width:190px}
.foot-brand .name{font-family:"IBM Plex Sans",sans-serif;font-weight:600;letter-spacing:1.5px;font-size:15px}
.foot-brand p{font-size:13px;line-height:16px;margin-top:14px}
.foot-brand a{color:var(--white);font-size:13px;display:inline-block;margin-top:8px}
.foot-links{position:absolute;left:320px;top:70px}
.foot-links ul{list-style:disc;margin:18px 0 0 16px;font-size:13px;line-height:20px}
.foot-contact{position:absolute;left:540px;top:70px;font-size:13px;line-height:20px}
.foot-contact dl{display:grid;grid-template-columns:26px 1fr;margin-top:18px;row-gap:6px}
.foot-sub{position:absolute;left:843px;top:70px;width:275px}
.foot-sub p{font-size:13px;margin-top:22px}
.foot-sub .email{margin-top:12px;height:38px;background:#2b2b2b;color:#aaa;font-size:12px;text-align:center;line-height:38px}
.foot-sub .submit{margin-top:8px;height:38px;background:var(--white);color:var(--ink);font-weight:700;font-size:14px;text-align:center;line-height:38px}
.bottom-bar{position:absolute;left:0;top:3856px;width:1200px;height:74px;background:var(--paper);font-size:12px;color:var(--text)}
.bottom-bar p{position:absolute;left:80px;top:29px}
.bottom-bar .social{right:82px;top:28px}
</style>
</head>
<body>

<header class="topbar">
  <div class="social"><span></span><span></span><span></span><span></span></div>
  <div class="brand">BELLHAVEN<small>FLOORING</small></div>
  <div class="callus">
    <svg width="26" height="26" viewBox="0 0 24 24" fill="none" stroke="#1d1d1d" stroke-width="1.6"><path d="M4 14v-2a8 8 0 0 1 16 0v2"/><rect x="3" y="13" width="4" height="6" rx="1"/><rect x="17" y="13" width="4" height="6" rx="1"/></svg>
    <div>Call Us Now:<br>+00 (0) 123 4560789</div>
  </div>
</header>

<nav class="mainnav">
  <a class="active" href="#">Home</a>
  <a href="#" style="left:204px">About us</a>
  <a href="#" style="left:347px">Services</a>
  <a href="#" style="left:490px">Gallery</a>
  <a href="#" style="left:633px">Blogs</a>
  <a href="#" style="left:776px">History</a>
  <a href="#" style="left:919px">Contact us</a>
  <svg class="search" width="24" height="24" viewBox="0 0 24 24" fill="none" stroke="#fff" stroke-width="2.4"><circle cx="10" cy="10" r="7"/><path d="M15 15l7 7"/></svg>
</nav>

<section class="hero">
  <div class="hero-photo" role="img" aria-label="Oak plank floor with a marble side table holding a notebook, camera and coffee cup"></div>
  <div class="hero-copy">
    <h1>Creating Your Exceptional<br>Wood Floor</h1>
    <a class="btn-outline" href="#">Read More</a>
  </div>
  <div class="dots"><i></i><i></i><i></i><i></i></div>
</section>

<section class="about">
  <h2>About us</h2>
  <p>BELLHAVEN offer a range of fully bespoke finished wood flooring in planks, herringbone blocks and chevrons; styles to suit any interior design.</p>
  <p>With endless options available, you can choose the design, dimensions, grade, texture, colour and finish all produced to order in the UK.Combining the finest sustainable CWS European Oak with the latest state of the art machinery, finishing products and highly skilled colour technicians, we will together create your bespoke wood floor.</p>
  <a class="btn" href="#">Read More</a>
</section>

<section class="services">
  <h2>Services</h2>
  <p class="lead">BELLHAVEN offer a range of fully bespoke finished wood flooring in planks,</p>
  <div class="service-list">
    <div class="service"><div class="photo" role="img" aria-label="Office with a wood plank floor and desk" style="background:radial-gradient(circle at 50% 70%,#9a6b44,#c9c3b8 70%)"></div><h3>Wood Flooring</h3><p>Lorem Ipsum is simply dummy of the printing and typesetting in the industry.</p><a href="#">Read More..</a></div>
    <div class="service"><div class="photo" role="img" aria-label="Kitchen with herringbone wood block floor" style="background:radial-gradient(circle at 50% 70%,#a06c43,#3a332d 75%)"></div><h3>Herringbone Blocks</h3><p>Lorem Ipsum is simply dummy of the printing and typesetting in the industry.</p><a href="#">Read More..</a></div>
    <div class="service"><div class="photo" role="img" aria-label="Bright room with a dark grey chevron floor" style="background:radial-gradient(circle at 50% 75%,#5d625c,#e4e6e1 70%)"></div><h3>Chevrons</h3><p>Lorem Ipsum is simply dummy of the printing and typesetting in the industry.</p><a href="#">Read More..</a></div>
    <div class="service"><div class="photo" role="img" aria-label="Living room with warm oak floor and white sofa" style="background:radial-gradient(circle at 50% 75%,#b77a45,#d8d3cc 70%)"></div><h3>Interior Design</h3><p>Lorem Ipsum is simply dummy of the printing and typesetting in the industry.</p><a href="#">Read More..</a></div>
  </div>
</section>

<section class="process">
  <div class="process-bg" role="img" aria-label="Pale whitewashed wood block floor texture"></div>
  <h2>THE BELLHAVEN PROCESS</h2>
  <div class="step" style="left:127px"><div class="num" style="background:var(--wood-dark)">01</div><p>Chosen Your<br>Design</p></div>
  <div class="step" style="left:381px"><div class="num" style="background:var(--wood-mid)">02</div><p>Chosen Your<br>Dimensions</p></div>
  <div class="step" style="left:634px"><div class="num" style="background:var(--wood-warm)">03</div><p>Chosen Your<br>Grade</p></div>
  <div class="step" style="left:885px"><div class="num" style="background:var(--wood-light)">04</div><p>Chosen Your<br>Finishes</p></div>
  <svg class="arrow" style="left:318px" width="56" height="40" viewBox="0 0 56 40"><path d="M4 30 Q24 6 44 16" fill="none" stroke="#111" stroke-width="7"/><path d="M38 4 L54 20 L34 26 Z" fill="#111"/></svg>
  <svg class="arrow" style="left:572px" width="56" height="40" viewBox="0 0 56 40"><path d="M4 30 Q24 6 44 16" fill="none" stroke="#111" stroke-width="7"/><path d="M38 4 L54 20 L34 26 Z" fill="#111"/></svg>
  <svg class="arrow" style="left:825px" width="56" height="40" viewBox="0 0 56 40"><path d="M4 30 Q24 6 44 16" fill="none" stroke="#111" stroke-width="7"/><path d="M38 4 L54 20 L34 26 Z" fill="#111"/></svg>
</section>

<section class="gallery">
  <h2>Gallery</h2>
  <div class="gallery-grid">
    <div role="img" aria-label="Pale herringbone floor close-up" style="background:linear-gradient(135deg,#e3ddd3,#cfc6b8)"></div>
    <div role="img" aria-label="Rich brown plank floor with a wicker chair" style="background:linear-gradient(160deg,#5a3a24,#9a6a42)"></div>
    <div role="img" aria-label="Light oak floor with a desk and chair by a window" style="background:linear-gradient(180deg,#ece8e2 40%,#b8875a)"></div>
    <div role="img" aria-label="Oak floor with a table and teal decor seen from above" style="background:linear-gradient(135deg,#8d6a48,#b98d5f 60%,#3f5c58)"></div>
    <div role="img" aria-label="Orange sofa on a light wood floor" style="background:linear-gradient(180deg,#e6e2dc 35%,#d06a2c 55%,#c59a6c)"></div>
    <div role="img" aria-label="Dark wood floor with framed pictures leaning on a wall" style="background:linear-gradient(160deg,#ededeb 30%,#5b4b40)"></div>
  </div>
  <a class="btn" href="#">View More</a>
</section>

<section class="history">
  <div class="history-copy">
    <h2>History</h2>
    <p>Lorem Ipsum is simply dummy text of the printing and wood typesetting industry.</p>
    <p>Lorem Ipsum has been the industry's standard dummy text a ever since the 1500s, when an unknown printer took a galley of type and scrambled it to make a type specimen book</p>
    <a class="btn" href="#">Read More</a>
  </div>
  <svg class="history-photos" viewBox="0 0 351 293" role="img" aria-label="Old oak tree trunk and green foliage in split panels">
    <defs><linearGradient id="leaf" x1="0" y1="0" x2="1" y2="1"><stop offset="0" stop-color="#7aa53a"/><stop offset=".55" stop-color="#4f6b2e"/><stop offset="1" stop-color="#2f3d22"/></linearGradient></defs>
    <rect x="0" y="0" width="286" height="293" fill="url(#leaf)"/>
    <rect x="292" y="0" width="59" height="58" fill="url(#leaf)"/>
    <rect x="292" y="64" width="59" height="160" fill="url(#leaf)"/>
    <rect x="292" y="230" width="59" height="63" fill="url(#leaf)"/>
  </svg>
</section>

<section class="contact">
  <div class="contact-bg" role="img" aria-label="Living room with wood block floor and a wire chair"></div>
  <h2>Contact us</h2>
  <div class="field" style="left:283px;top:100px;width:192px">Name</div>
  <div class="field" style="left:497px;top:100px;width:193px">Phone</div>
  <div class="field" style="left:712px;top:100px;width:194px">Email</div>
  <div class="field" style="left:283px;top:150px;width:623px;height:115px">Message</div>
  <a class="btn" href="#">Send More</a>
</section>

<footer class="site-footer">
  <div class="foot-brand">
    <div class="name">BELLHAVEN</div>
    <p>Lorem Ipsum is simply a dummy text of the print typesetting industry.</p>
    <a href="#">Read More..</a>
  </div>
  <div class="foot-links">
    <h4>Quick Link</h4>
    <ul><li>Home</li><li>About us</li><li>Services</li><li>Gallery</li><li>History</li><li>Contact us</li></ul>
  </div>
  <div class="foot-contact">
    <h4>Contact us</h4>
    <dl>
      <dt>A :</dt><dd>123th Street,<br>City, UK</dd>
      <dt>P :</dt><dd>+44 (0)208 431 9052<br>+44 (0) 7700 824 319</dd>
      <dt>E :</dt><dd>enquire@bellhaven.co.uk.com</dd>
    </dl>
  </div>
  <div class="foot-sub">
    <h4>Subscribe to our newsletter</h4>
    <p>To receive the latest news &amp; update</p>
    <div class="email">Email Here</div>
    <div class="submit">Submit</div>
  </div>
</footer>

<div class="bottom-bar">
  <p>Copyright © Bellhaven. All Right Reserved</p>
  <div class="social"><span></span><span></span><span></span><span></span><span></span></div>
</div>

</body>
</html>
```